Exceptional Corporate Business Card Design

Hello,

We need an exceptional corporate business card design based on our logo attached. We require:

1. A Variation for letterpress print
2. Standard size of business card 84mm x 55mm (Artwork 88mm x 59mm)
3. Variation for square business card 65mm x 65mm (Artwork 69mm x 69mm)
4. Variation as a one side print
5. Adobe Illustrator files

The company is in the financial industry, valmisto.com

The logo is attached as vector pdf.
regards

```html
<!DOCTYPE html>
<html lang="en">
<head>
<meta charset="utf-8">
<title>Valmisto – Business Card</title>
<link href="https://fonts.googleapis.com/css2?family=Questrial&family=Arimo:wght@400&display=swap" rel="stylesheet">
<style>
  :root {
    --brand-blue: #3b3a92;
    --brand-blue-deep: #2f2e86;
    --paper: #ffffff;
    --ink: #141414;
    --backdrop: #e9e7e4;
  }
  html, body {
    margin: 0;
    padding: 0;
    width: 1200px;
    height: 914px;
    overflow: hidden;
    background: var(--backdrop);
  }
  .sheet {
    position: relative;
    width: 1200px;
    height: 914px;
  }
  .card {
    position: absolute;
    top: 282px;
    width: 520px;
    height: 349px;
    box-shadow: 0 6px 18px rgba(0,0,0,0.18);
    overflow: hidden;
  }
  .card--front { left: 50px; background: var(--paper); }
  .card--back {
    left: 630px;
    background: linear-gradient(135deg, var(--brand-blue), var(--brand-blue-deep));
  }
  .wordmark {
    display: flex;
    align-items: center;
    gap: 10px;
    color: var(--brand-blue);
    font-family: "Questrial", sans-serif;
    font-size: 54px;
    letter-spacing: 1px;
    line-height: 1;
  }
  .wordmark__dot {
    width: 66px;
    height: 66px;
    border-radius: 50%;
    background: var(--brand-blue);
    flex: none;
  }
  .card--front .wordmark {
    position: absolute;
    left: 34px;
    top: 44px;
  }
  .contact {
    position: absolute;
    right: 28px;
    bottom: 30px;
    margin: 0;
    padding: 0;
    list-style: none;
    font-family: "Arimo", sans-serif;
    font-size: 14px;
    color: var(--ink);
    text-align: right;
  }
  .contact li {
    display: flex;
    justify-content: flex-end;
    align-items: center;
    gap: 10px;
    line-height: 20px;
  }
  .contact svg { width: 12px; height: 12px; flex: none; }
  .band {
    position: absolute;
    left: 0;
    right: 0;
    top: 84px;
    height: 120px;
    background: var(--paper);
    display: flex;
    align-items: center;
    justify-content: center;
  }
</style>
</head>
<body>
<main class="sheet">
  <section class="card card--front" aria-label="Business card front">
    <div class="wordmark"><span class="wordmark__dot"></span>VALMISTO</div>
    <ul class="contact">
      <li>www.valmisto.com
        <svg viewBox="0 0 12 12" aria-hidden="true"><circle cx="6" cy="6" r="5.5" fill="var(--brand-blue)"/><path d="M1 6h10M6 1c-2.5 3-2.5 7 0 10M6 1c2.5 3 2.5 7 0 10" stroke="#fff" stroke-width="0.8" fill="none"/></svg>
      </li>
      <li>office@valmisto.com
        <svg viewBox="0 0 12 12" aria-hidden="true"><rect x="0.5" y="2" width="11" height="8" fill="var(--brand-blue)"/><path d="M0.5 2l5.5 4.5L11.5 2" stroke="#fff" stroke-width="0.9" fill="none"/></svg>
      </li>
      <li>24-26 Larch Street, W2R 7QP, London, England
        <svg viewBox="0 0 12 12" aria-hidden="true"><path d="M6 11.5C3 8 2 6.5 2 4.8a4 4 0 0 1 8 0C10 6.5 9 8 6 11.5z" fill="var(--brand-blue)"/><circle cx="6" cy="4.8" r="1.5" fill="#fff"/></svg>
      </li>
    </ul>
  </section>

  <section class="card card--back" aria-label="Business card back">
    <div class="band">
      <div class="wordmark"><span class="wordmark__dot"></span>VALMISTO</div>
    </div>
  </section>
</main>
</body>
</html>
```